Sleek, Professional Business Card Design Needed

Business Cards - Logo Attached.

We are a solar consulting company. We are national and want our cards to represent the professional high quality products that we offer.

Industry/Entity Type

Business

Contact Information for Business Card

n/a

Requirements
Must have
• Design
• Name
• Position
• Number
• Email
• Address
Should not have
• Not be too crowded

```html
<!DOCTYPE html>
<html lang="en">
<head>
<meta charset="utf-8">
<title>Bright Meridian Solar – Business Card</title>
<link rel="stylesheet" href="https://fonts.googleapis.com/css2?family=Montserrat:wght@400;700&display=swap">
<style>
  :root {
    --green: #9ac63b;
    --blue: #0591cc;
    --tab-dark: #5b5b5b;
    --tab-mid: #999999;
    --tab-light: #d0d0d0;
    --white: #ffffff;
  }
  * { margin: 0; padding: 0; box-sizing: border-box; }
  html, body {
    width: 1200px; height: 686px; overflow: hidden; background: var(--white);
  }
  .card {
    position: relative; width: 1200px; height: 686px;
    background: var(--white);
    font-family: "Montserrat", "Century Gothic", sans-serif;
  }
  .accent-strip {
    position: absolute; left: 0; top: 0; width: 61px; height: 686px;
    background: var(--green);
  }
  .info-panel {
    position: absolute; left: 61px; top: 0; width: 628px; height: 686px;
    background: var(--blue); color: var(--white);
  }
  .label-tab {
    position: absolute; left: 0; width: 61px; height: 110px;
    display: flex; align-items: center; justify-content: center;
  }
  .label-tab span {
    transform: rotate(-90deg); white-space: nowrap;
    font-size: 11px; letter-spacing: 0.5px; color: var(--white);
  }
  .tab-contact { top: 275px; background: var(--tab-dark); }
  .tab-email { top: 385px; background: var(--tab-mid); }
  .tab-address { top: 495px; background: var(--tab-light); }

  .person-name {
    position: absolute; left: 22px; top: 90px;
    font-size: 43px; font-weight: 700; letter-spacing: -0.3px;
  }
  .person-position {
    position: absolute; left: 22px; top: 148px;
    font-size: 23px; font-weight: 400; letter-spacing: 0.5px;
  }
  .contact-line {
    position: absolute; left: 22px;
    font-size: 31px; font-weight: 400; letter-spacing: 0.3px;
  }
  .contact-phone { top: 312px; }
  .contact-email { top: 421px; }
  .contact-address { top: 530px; }

  .brand {
    position: absolute; left: 689px; top: 0; width: 511px; height: 686px;
    display: flex; flex-direction: column; align-items: center; justify-content: center;
    padding-top: 120px; gap: 22px;
  }
  .brand-dot { width: 120px; height: 120px; }
  .brand-name {
    color: var(--blue); font-size: 40px; font-weight: 700;
    text-align: center; line-height: 1.15;
  }
</style>
</head>
<body>
  <div class="card">
    <div class="accent-strip"></div>
    <div class="label-tab tab-contact"><span>CONTACT NO.</span></div>
    <div class="label-tab tab-email"><span>EMAIL ADD</span></div>
    <div class="label-tab tab-address"><span>ADDRESS</span></div>

    <section class="info-panel">
      <h1 class="person-name">Last, First Name</h1>
      <p class="person-position">POSITION</p>
      <p class="contact-line contact-phone">(00)123.4567</p>
      <p class="contact-line contact-email">brightmeridiansolar@mail.com</p>
      <p class="contact-line contact-address">12 ABC Bldg. State, Country</p>
    </section>

    <div class="brand">
      <svg class="brand-dot" viewBox="0 0 120 120" aria-hidden="true">
        <circle cx="60" cy="60" r="60" fill="var(--green)"/>
      </svg>
      <p class="brand-name">BRIGHT MERIDIAN<br>SOLAR</p>
    </div>
  </div>
</body>
</html>
```